Stationary design and implementation for Swedish IT company

Hi,

I'm looking for a design and statiionary for my company (www.lumenfarro.example).

LumenFarro is an innovative company with four core values:
- Entrepreneurial; we take risks and the responsibility to create value
- Awarding; we work with fun and have added value to our relationships
- Innovation; we're creative and introduce new solutions
- Respect; we work with respect for our environment based on values instead of red tape

The required stationary should include:
- Powerpoint template
- Word templates
- Business card design
- e-mail signature

Please visit our site for more details.
Updates

Hi - please read (PRIORITY!),

You have been involved in one my projects. 

As it seems there is something seriously wrong with the participation payments at ArtHively. 

I have send invites with participation payments to reward designers for there work. It has been reported that these invitations resulted in expired messages, and payments have NOT been made. The money is withdrawn from my account and NOT paid to designers. This is a real shame when people do not get rewarded for the work done and the money is gone.

When you got an invitation with participation payment could you please let me know if the payment has actually been made? You can contact me at kmelvane@lumenfarro.example.

I'm trying to get this clarified with ArtHively.

Grt, Kees

Target Market(s)

Our market is IT and professional service in Sweden and other Nordics countries (Danmark, Norway, Finland).

Industry/Entity Type

Environment

Requirements
Must have
• Project delivery should include:
- Powerpoint template with title and content pages
- Standard letter (Word template)
- Standard invoice (Word template)
- Business card
- e-mail signature
Should not have
• Please await a logo to be attached (almost done).

```html
<!DOCTYPE html>
<html lang="en">
<head>
<meta charset="utf-8">
<title>LumenFarro stationery</title>
<link href="https://fonts.googleapis.com/css2?family=Open+Sans:wght@400;600&display=swap" rel="stylesheet">
<style>
  :root {
    --page: #ffffff;
    --edge: #a9a9a9;
    --ink: #222222;
    --brand: #2f3f8f;
    --brand-dot: #3d6fc4;
    --rule: #b8b8b8;
    --accent: #e8772a;
    --accent-light: #f6b27a;
  }
  * { box-sizing: border-box; margin: 0; padding: 0; }
  html, body { width: 1200px; height: 900px; overflow: hidden; background: var(--page); }
  body { position: relative; font-family: "Open Sans", Arial, sans-serif; color: var(--ink); }

  .sheet { position: absolute; background: var(--page); border: 1px solid var(--edge); box-shadow: 0 1px 3px rgba(0,0,0,0.12); }

  .brand { position: absolute; display: flex; align-items: center; gap: 0.35em; color: var(--brand); font-weight: 400; white-space: nowrap; }
  .brand-dot { width: 0.7em; height: 0.7em; border-radius: 50%; background: var(--brand-dot); flex: none; }

  .v-rule { position: absolute; width: 3px; background: linear-gradient(to bottom, rgba(150,150,150,0), #9a9a9a 50%, rgba(150,150,150,0)); }

  /* Wide business card */
  .card-wide { left: 24px; top: 24px; width: 532px; height: 292px; }
  .card-wide .contact { position: absolute; right: 308px; text-align: right; }
  .card-wide .name { top: 58px; font-size: 17px; }
  .card-wide .email { top: 92px; font-size: 14px; }
  .card-wide .phone { top: 158px; font-size: 12px; }
  .card-wide .address { top: 194px; font-size: 12px; }
  .card-wide .v-rule { left: 234px; top: 10px; height: 270px; }
  .card-wide .brand { left: 250px; top: 112px; font-size: 40px; }

  /* Compact business card */
  .card-compact { left: 134px; top: 354px; width: 292px; height: 204px; }
  .card-compact .v-rule { left: 24px; top: 14px; height: 96px; }
  .card-compact .name { position: absolute; left: 46px; top: 24px; font-size: 15px; }
  .card-compact .role { position: absolute; left: 46px; top: 46px; font-size: 11px; }
  .card-compact .email { position: absolute; left: 46px; top: 74px; font-size: 11px; }
  .card-compact .h-rule { position: absolute; left: 6px; right: 6px; top: 116px; height: 2px; background: #555; }
  .card-compact .brand { left: 22px; top: 132px; font-size: 38px; }

  /* Slide template */
  .slide { left: 76px; top: 596px; width: 430px; height: 278px; }
  .slide .feature { position: absolute; left: 134px; top: 46px; width: 140px; height: 134px; border-radius: 26px; background: linear-gradient(160deg, var(--accent-light), var(--accent)); }
  .slide .divider { position: absolute; left: 14px; right: 14px; top: 214px; height: 3px; background: linear-gradient(to right, rgba(180,180,180,0), #bdbdbd 50%, rgba(180,180,180,0)); }
  .slide .brand { left: 26px; top: 226px; font-size: 22px; }

  /* Letterhead */
  .letter { left: 592px; top: 80px; width: 584px; height: 752px; }
  .letter .brand { left: 66px; top: 32px; font-size: 24px; }
  .letter .footer-rule { position: absolute; left: 68px; width: 450px; top: 692px; height: 1px; background: var(--rule); }
  .letter .footer { position: absolute; right: 64px; top: 698px; font-size: 8px; color: #333; }
  .letter .footer strong { font-weight: 600; }
</style>
</head>
<body>

  <section class="sheet card-wide" aria-label="Business card, wide">
    <p class="contact name">Your name</p>
    <p class="contact email">email@yourdomain.com</p>
    <p class="contact phone">Your telephone</p>
    <p class="contact address">Your Address</p>
    <div class="v-rule"></div>
    <div class="brand"><span class="brand-dot"></span>LumenFarro</div>
  </section>

  <section class="sheet card-compact" aria-label="Business card, compact">
    <div class="v-rule"></div>
    <p class="name">Your name</p>
    <p class="role">Director</p>
    <p class="email">email@yourdomain.com</p>
    <div class="h-rule"></div>
    <div class="brand"><span class="brand-dot"></span>LumenFarro</div>
  </section>

  <section class="sheet slide" aria-label="Presentation title slide">
    <div class="feature" role="img" aria-label="Presentation software badge"></div>
    <div class="divider"></div>
    <div class="brand"><span class="brand-dot"></span>LumenFarro</div>
  </section>

  <section class="sheet letter" aria-label="Letterhead">
    <div class="brand"><span class="brand-dot"></span>LumenFarro</div>
    <div class="footer-rule"></div>
    <p class="footer"><strong>Office 12,</strong> 18 Kungsgatan, Uppsala, Sweden, 753 21</p>
  </section>

</body>
</html>
```